Innovative Consulting Firm Needs New Business Cards and Stationary

Our Innovative Consulting Firm, Larkfield Consulting, is in need of new business cards and stationary designs. We want two-sided cards that incorporate our logo, which is attached. We are looking for something not too formal, but is professional and slick.

Card should have the following information:
Name (ex. Tom Bradley)
Title (ex. Manager)
Address (ex. 24680 Cedar Lane)
Address 2 (ex. Suite 100)
City
State
Zip Code
Mobile
Email

The card should also have our website: www.larkfieldconsulting.example

Industry/Entity Type

Management Consulting

Contact Information for Business Card

Name (ex. Tom Bradley)
Title (ex. Manager)
Address 2 (ex. Suite 100)
City
State
Zip Code
Mobile
Email

Font styles to use
Sans Serif

Requirements
Must have
• The colors on the card must match the colors in the logo. The exact color codes are attached in a pdf.
Nice to have
• The Company's Tagline is "Focused on your Future". This might be nice to incorporate, but not necessary.

```html
<!DOCTYPE html>
<html lang="en">
<head>
<meta charset="utf-8">
<title>Larkfield Consulting — Stationery</title>
<link rel="stylesheet" href="https://fonts.googleapis.com/css2?family=Lato:ital,wght@0,400;0,700;0,900;1,700;1,900&display=swap">
<style>
  :root {
    --navy: #224f7a;
    --gold: #f3b11b;
    --paper: #ffffff;
    --backdrop: #b9b9b9;
  }
  html, body {
    margin: 0;
    padding: 0;
    width: 1200px;
    height: 994px;
    overflow: hidden;
    background: var(--backdrop);
    font-family: "Lato", Arial, sans-serif;
  }
  .sheet {
    position: absolute;
    background: var(--paper);
    box-shadow: 0 1px 5px rgba(0,0,0,0.25);
    overflow: hidden;
  }
  .sheet > svg { position: absolute; left: 0; top: 0; }
  .letterhead { left: 84px; top: 24px; width: 504px; height: 652px; }
  .folder { left: 612px; top: 24px; width: 504px; height: 652px; }
  .envelope-back { left: 24px; top: 726px; width: 564px; height: 244px; }
  .envelope-flap { left: 612px; top: 726px; width: 564px; height: 244px; }

  .brand { position: absolute; color: var(--navy); font-weight: 700; line-height: 1; }
  .brand .brand-name { display: block; letter-spacing: 0.5px; }
  .brand .brand-sub { display: block; text-align: right; letter-spacing: 0.35em; margin-top: 3px; }
  .brand.on-dark { color: var(--paper); }

  .letterhead .brand { left: 24px; top: 24px; }
  .letterhead .brand-name { font-size: 34px; }
  .letterhead .brand-sub { font-size: 8px; }

  .contact-list {
    position: absolute; left: 380px; top: 24px;
    margin: 0; padding: 0; list-style: none;
    color: var(--navy); font-size: 7px; font-weight: 700; line-height: 9px;
  }
  .contact-list li { display: flex; gap: 4px; }
  .contact-list svg { flex: none; margin-top: 1px; }

  .web-address {
    position: absolute; color: var(--paper); font-size: 9px; font-weight: 400;
    transform: translateX(-50%); white-space: nowrap;
  }
  .web-address b { font-weight: 700; }
  .letterhead .web-address { left: 364px; top: 632px; }

  .folder .brand { left: 48px; top: 76px; }
  .folder .brand-name { font-size: 58px; }
  .folder .brand-sub { font-size: 12px; margin-top: 6px; }
  .tagline {
    position: absolute; right: 24px; top: 540px;
    color: var(--navy); font-size: 22px; font-weight: 900; font-style: italic;
  }

  .envelope-back .brand { left: 12px; top: 16px; }
  .envelope-back .brand-name { font-size: 24px; }
  .envelope-back .brand-sub { font-size: 6px; }
  .return-address {
    position: absolute; left: 12px; top: 54px;
    color: var(--paper); font-size: 7px; font-weight: 700; line-height: 8.5px;
  }

  .envelope-flap .brand { left: 50%; top: 22px; transform: translateX(-50%); }
  .envelope-flap .brand-name { font-size: 24px; }
  .envelope-flap .brand-sub { font-size: 6px; }
  .envelope-flap .web-address { left: 406px; top: 226px; font-size: 8.5px; }
</style>
</head>
<body>

<section class="sheet letterhead" aria-label="Letterhead">
  <svg width="504" height="652" viewBox="0 0 504 652">
    <path d="M136,652 C250,612 400,606 504,640 L504,652 Z" fill="var(--gold)"/>
    <path d="M182,652 C300,620 420,618 504,646 L504,652 Z" fill="var(--navy)" stroke="var(--paper)" stroke-width="1"/>
  </svg>
  <div class="brand"><span class="brand-name">Larkfield</span><span class="brand-sub">CONSULTING</span></div>
  <ul class="contact-list">
    <li><svg width="7" height="7" viewBox="0 0 10 10"><circle cx="5" cy="5" r="5" fill="var(--navy)"/><circle cx="5" cy="4.3" r="1.8" fill="#fff"/></svg><span>24680 Cedar Lane Suite 100<br>Fairhaven, TX 75001</span></li>
    <li><svg width="7" height="7" viewBox="0 0 10 10"><circle cx="5" cy="5" r="5" fill="var(--navy)"/><rect x="2.5" y="3.3" width="5" height="3.4" fill="#fff"/></svg><span>info@larkfieldconsulting.example</span></li>
    <li><svg width="7" height="7" viewBox="0 0 10 10"><circle cx="5" cy="5" r="5" fill="var(--navy)"/><path d="M3,3 L4.3,3 L4.8,4.4 L4.1,5 Q4.8,6.2 5.9,6.4 L6.5,5.7 L7.5,6.2 L7.3,7.3 Q3.4,7.2 3,3 Z" fill="#fff"/></svg><span>555-010-4821</span></li>
  </ul>
  <div class="web-address">www.<b>larkfieldconsulting.example</b></div>
</section>

<section class="sheet folder" aria-label="Presentation folder">
  <svg width="504" height="652" viewBox="0 0 504 652">
    <rect width="504" height="652" fill="var(--navy)"/>
    <path d="M0,557 C110,480 240,440 340,450 C420,455 470,462 504,474" fill="none" stroke="var(--paper)" stroke-width="1.5"/>
    <path d="M0,560 C110,484 240,444 340,454 C420,459 470,466 504,476 L504,652 L0,652 Z" fill="var(--gold)"/>
    <path d="M0,596 C120,510 250,470 350,474 C420,477 470,482 504,478 L504,652 L0,652 Z" fill="var(--paper)"/>
  </svg>
  <div class="brand on-dark"><span class="brand-name">Larkfield</span><span class="brand-sub">CONSULTING</span></div>
  <div class="tagline">Focused on your Future...</div>
</section>

<section class="sheet envelope-back" aria-label="Envelope front">
  <svg width="564" height="244" viewBox="0 0 564 244">
    <path d="M0,0 H564 V46 C530,30 470,14 400,14 C260,14 120,80 0,174 Z" fill="var(--gold)"/>
    <path d="M0,0 H564 V40 C530,26 470,10 390,10 C250,10 110,60 0,140 Z" fill="var(--navy)" stroke="var(--paper)" stroke-width="1"/>
  </svg>
  <div class="brand on-dark"><span class="brand-name">Larkfield</span><span class="brand-sub">CONSULTING</span></div>
  <div class="return-address">24680 Cedar Lane Suite 100<br>Fairhaven, TX 75001</div>
</section>

<section class="sheet envelope-flap" aria-label="Envelope back">
  <svg width="564" height="244" viewBox="0 0 564 244">
    <path d="M0,0 H564 L552,72 H12 Z" fill="var(--navy)"/>
    <path d="M176,244 C270,214 420,206 564,232 L564,244 Z" fill="var(--gold)"/>
    <path d="M224,244 C320,222 450,218 564,238 L564,244 Z" fill="var(--navy)" stroke="var(--paper)" stroke-width="1"/>
  </svg>
  <div class="brand on-dark"><span class="brand-name">Larkfield</span><span class="brand-sub">CONSULTING</span></div>
  <div class="web-address">www.<b>larkfieldconsulting.example</b></div>
</section>

</body>
</html>
```